Pagina Lartécnica

The Lartécnica is a company dealing with leasing and selling real estate. The current site can be accessed at www.lartecnica-exemplo.com.br. We intend to redesign the look of the site and for that we would like to redesign the home page and the page with information and pictures of the property. The homepage should maintain the characteristics of the current common design simple, short and straightforward. The page with the data of the properties should be accessed with two changes page as it is currently running. The search from the map by region and should be maintained.
The page containing the information of the property will provide a total of 15 small pictures that when clicked will appear in larger size. The colors to be used should be orange, blue, black and white. The map can be maintained in the current colors.
Updates

Project Deadline Extended
Reason: Payment guarante!!

Payment guaranteed. Deadline for submission of designs April 27.

Industry/Entity Type

Real Estate

Requirements
Must have
• Search by map regions and search box
address
keep colors from the current page
phones
clean look
Nice to have
• clean look
Should not have
• We like the current page. We just want to make it compatible with modern and new design trends and monitors.

```html
<!DOCTYPE html>
<html lang="en">
<head>
<meta charset="utf-8">
<title>Lartécnica – Real Estate</title>
<link href="https://fonts.googleapis.com/css2?family=Arimo:wght@400;700&family=Open+Sans:wght@400;600;700&family=Oswald:wght@400;500&family=Roboto+Condensed:wght@400;700&family=Ubuntu:wght@400;500&display=swap" rel="stylesheet">
<style>
:root{
  --purple:#4f4a6b;
  --purple-dark:#3f3a58;
  --orange:#f58220;
  --orange-dark:#e36c0a;
  --orange-text:#f07a14;
  --ink:#3c3c3c;
  --body:#222;
  --white:#fff;
  --hero-dark:#2e2a33;
  --hero-mid:#4a4450;
}
*{box-sizing:border-box;margin:0;padding:0}
html,body{width:1200px;height:1095px;overflow:hidden;background:var(--white)}
body{position:relative;font-family:"Arimo",Arial,sans-serif;color:var(--body)}
.abs{position:absolute}

/* header */
.brand{left:102px;top:50px;display:flex;align-items:center;gap:12px}
.brand-mark{width:30px;height:30px;background:var(--purple)}
.brand-name{font-family:"Open Sans",sans-serif;font-weight:700;font-size:40px;color:var(--purple);letter-spacing:-1px}
.contact{right:142px;top:45px;text-align:right;font-family:"Arimo",sans-serif;font-size:13.5px;font-weight:700;color:#333;white-space:nowrap}
.contact .hl{color:var(--orange)}
.contact-rule{left:732px;top:65px;width:326px;border-top:1px dotted #999}
.tollfree{left:732px;top:64px;width:326px;height:41px;border-bottom:1px dotted #999;display:flex;align-items:center;gap:7px;white-space:nowrap}
.tollfree .phone-icon{flex:none;width:30px;height:30px;border-radius:4px;background:var(--orange);display:flex;align-items:center;justify-content:center}
.tollfree .label{flex:none;font-family:"Oswald",sans-serif;font-size:19px;line-height:1;color:#222}
.tollfree .num{flex:none;margin-left:auto;font-family:"Oswald",sans-serif;font-size:23px;line-height:1;color:#f6a51c}

/* nav */
.nav{left:0;top:146px;width:1200px;height:53px;background:var(--purple);border-bottom:3px solid var(--orange)}
.nav ul{list-style:none;position:absolute;left:0;top:0;height:50px;width:1200px}
.nav li{position:absolute;top:19px;font-family:"Ubuntu",sans-serif;font-size:14px;color:var(--white);white-space:nowrap}
.nav li.active{left:116px;top:8px;width:59px;height:42px;background:var(--orange);border-radius:4px 4px 0 0;text-align:center;padding-top:11px}

/* hero */
.hero{left:0;top:199px;width:1200px;height:376px;background:radial-gradient(ellipse at 65% 45%,var(--hero-mid),var(--hero-dark) 75%)}
.hero h1{position:absolute;left:113px;top:40px;font-family:"Roboto Condensed",sans-serif;font-weight:400;font-size:31px;line-height:38px;color:var(--white);white-space:nowrap}
.hero h1 em{font-style:normal;color:var(--orange)}
.hero p{position:absolute;left:113px;top:128px;width:390px;font-family:"Open Sans",sans-serif;font-weight:600;font-size:14px;line-height:20px;color:var(--white)}
.cta{position:absolute;left:111px;top:257px;width:313px;height:54px;border-radius:27px;background:linear-gradient(#fff,#d8d8d8);overflow:hidden;display:flex;align-items:center}
.cta span{font-family:"Open Sans",sans-serif;font-weight:600;font-size:24px;color:#3d3d3d;padding-left:10px;flex:1;white-space:nowrap}
.cta i{width:38px;height:54px;background:var(--orange-dark);display:flex;align-items:center;justify-content:center}
.hero-photo{position:absolute;left:560px;top:0;width:430px;height:370px;border-radius:40% 40% 45% 45%;background:radial-gradient(ellipse at 50% 45%,#e9863e 0%,#c89a86 40%,rgba(90,80,90,0) 72%)}

/* search band */
.search{left:0;top:575px;width:1200px;height:73px;background:linear-gradient(var(--orange),var(--orange-dark))}
.search-title{position:absolute;left:103px;top:14px;height:49px;width:358px;background:var(--purple);clip-path:polygon(0 0,93% 0,100% 50%,93% 100%,0 100%);border-radius:6px 0 0 6px;font-family:"Open Sans",sans-serif;font-weight:600;font-size:27px;color:var(--white);padding:4px 0 0 14px;white-space:nowrap}
.radio{position:absolute;top:30px;font-family:"Arimo",sans-serif;font-weight:700;font-size:15px;color:var(--white);display:flex;align-items:center;gap:9px;white-space:nowrap}
.radio b{width:12px;height:12px;border-radius:50%;background:#eee;border:1px solid #aaa;display:inline-block}
.radio b.on{background:radial-gradient(#2c5a8a 35%,#eee 40%)}
.select{position:absolute;left:694px;top:27px;width:141px;height:25px;background:var(--white);border:1px solid #ccc;font-size:13px;color:#aaa;padding:3px 0 0 12px}
.select::after{content:"";position:absolute;right:6px;top:9px;border:5px solid transparent;border-top-color:#333}
.btn-search{position:absolute;left:872px;top:22px;width:122px;height:33px;border-radius:17px;background:var(--purple);border:2px solid #8a86a4;color:var(--white);font-family:"Arimo",sans-serif;font-weight:700;font-size:14px;letter-spacing:.5px;display:flex;align-items:center;gap:6px;padding-left:10px}

/* content */
.intro{left:102px;top:688px;width:692px}
.intro h2{font-family:"Open Sans",sans-serif;font-weight:600;font-size:24px;color:var(--ink);white-space:nowrap}
.intro h3{font-family:"Arimo",sans-serif;font-weight:700;font-size:18px;color:var(--orange-dark);margin:6px 0 0 2px;white-space:nowrap}
.intro p{font-size:13px;line-height:20px;letter-spacing:.12px;color:var(--body);text-align:justify;margin-top:16px}
.intro p + p{margin-top:20px}

.region{left:826px;top:680px;width:265px;height:301px;border:1px solid #ddd;border-radius:8px;background:linear-gradient(#fafafa,#e9e9e9)}
.region h4{position:absolute;left:14px;top:13px;font-family:"Oswald",sans-serif;font-weight:400;font-size:19px;color:var(--purple);white-space:nowrap}
.region h4 em{font-style:normal;color:var(--orange)}
.region-map{position:absolute;left:14px;top:54px;width:238px;height:232px;border:1px solid #bbb;background:linear-gradient(120deg,#9ec9e8 0%,#f2e4c2 35%,#8fc0e2 55%,#efe0bd 75%,#9ec9e8 100%)}

/* footer */
.footer{left:0;top:1007px;width:1200px;height:88px;background:var(--purple)}
.footer address{position:absolute;left:114px;top:15px;font-style:normal;font-family:"Open Sans",sans-serif;font-weight:600;font-size:13px;line-height:24px;color:var(--white);white-space:nowrap}
.footer .brand-foot{position:absolute;left:920px;top:30px;display:flex;align-items:center;gap:10px}
.footer .brand-foot .brand-mark{background:var(--white);width:26px;height:26px}
.footer .brand-foot .brand-name{color:var(--white);font-size:30px}
</style>
</head>
<body>

<header>
  <div class="abs brand"><span class="brand-mark"></span><span class="brand-name">Lartécnica</span></div>
  <div class="abs contact"><span class="hl">info</span>@lartecnica-exemplo.com.br &nbsp;<span class="hl">Fax:</span> 604-555-0192</div>
  <div class="abs contact-rule"></div>
  <div class="abs tollfree">
    <span class="phone-icon"><svg width="18" height="18" viewBox="0 0 24 24"><path fill="#fff" d="M6.6 10.8c1.4 2.8 3.8 5.1 6.6 6.6l2.2-2.2c.3-.3.7-.4 1-.2 1.1.4 2.3.6 3.6.6.6 0 1 .4 1 1V20c0 .6-.4 1-1 1C10.6 21 3 13.4 3 4c0-.6.4-1 1-1h3.5c.6 0 1 .4 1 1 0 1.3.2 2.5.6 3.6.1.3 0 .7-.2 1z"/></svg></span>
    <span class="label">CALL US TOLL-FREE ON</span><span class="num">1800 555 318</span>
  </div>
</header>

<nav class="abs nav">
  <ul>
    <li class="active">Home</li>
    <li style="left:211px">Location</li>
    <li style="left:313px">Restricted Area</li>
    <li style="left:459px">List your property</li>
    <li style="left:621px">Owner Info</li>
    <li style="left:741px">Information for Tenant</li>
    <li style="left:939px">Request your property</li>
  </ul>
</nav>

<section class="abs hero">
  <h1>The Lartécnica, for over fifteen<br>years in the <em>real estate market...</em></h1>
  <p>permeated the culture and values defined by the needs of its customers, is gradually building a solid body for the management of real estate. These and adversity, brought him the wisdom necessary to build step by step a large gap in the provision of its services.</p>
  <div class="cta"><span>Request your property</span><i><svg width="24" height="24" viewBox="0 0 24 24" fill="none" stroke="#fff" stroke-width="2"><path d="M5 5l7 7-7 7M12 5l7 7-7 7"/></svg></i></div>
  <div class="hero-photo" role="img" aria-label="Photo of cupped hands holding a small house with an orange tiled roof"></div>
</section>

<section class="abs search">
  <div class="search-title">Search for Properties</div>
  <div class="radio" style="left:519px"><b></b>The Buy</div>
  <div class="radio" style="left:620px"><b class="on"></b>Rent</div>
  <div class="select">Every</div>
  <div class="btn-search"><svg width="26" height="18" viewBox="0 0 26 18" fill="none" stroke="#fff" stroke-width="1.6"><circle cx="8" cy="8" r="6"/><path d="M3 8h10M8 2v12M13 12l8 5"/></svg>BUSCAR</div>
</section>

<main>
  <article class="abs intro">
    <h2>The Lartécnica, for over fifteen years...</h2>
    <h3>A service company must always be in line with the market.</h3>
    <p>The Lartécnica, for over fifteen years in the real estate market, permeated the culture and values defined by the needs of its customers, is gradually building a solid body for the management and sale of real estate. These years marked by moments of achievement and adversity, brought him the wisdom necessary to build step by step a large gap in the provision of its services.Bring happiness to relationships, provide solidity to the continuing purpose of serving, has been objectively the character of their actions.</p>
    <p>Movements in search of a personalized service have the convenience of the Customer, its greater purpose. Has been its commitment to sustain permanently ethical management, fully honoring all financial commitments and tax, making transparent the relationship with clients, be they owners,</p>
  </article>

  <aside class="abs region">
    <h4>SEARCH <em>PROPERTY BY REGION</em></h4>
    <div class="region-map" role="img" aria-label="Regional map of the island and coastline for searching properties by area"></div>
  </aside>
</main>

<footer class="abs footer">
  <address>Rua das Acácias, 48 - Street Corner with Marcos Lemos - Centro Vila Serena -<br>CEP: 00000-100 - Fax: (48) 3555-0147</address>
  <div class="brand-foot"><span class="brand-mark"></span><span class="brand-name">Lartécnica</span></div>
</footer>

</body>
</html>
```